Make a medical leaflet for my patients undergoing ankle blocks

I have a very boring text only leaflet I would like to turn into a professional appealing medical leaflet to give to my patients. I would like to get this onto two pages of a4 if possible and its intended for electronic distribution mainly.
This will be for patients so it must be professional.
It must also contain a copyright logo on it and my name near the start (Dr Tobias Wendell) so my colleagues can't use it easily.
Target Market(s)
Patients undergoing surgery
Industry/Entity Type
Medical
Font styles to use
Other font styles liked:
- no idea, you tell me
Requirements
Must have
- the information contained on the attachment
- look professional
- a copyright on it
Nice to have
- the ashbury clinic logo
Should not have
- Any spelling, grammatical or linguistic errors
- Any font less than size 12

```html
<!DOCTYPE html>
<html lang="en">
<head>
<meta charset="utf-8">
<title>Ankle Block – Patient Information</title>
<link href="https://fonts.googleapis.com/css2?family=Open+Sans:wght@400;600;700;800&display=swap" rel="stylesheet">
<style>
  :root {
    --navy: #1d2a57;
    --red: #c8102e;
    --text: #4a4f5c;
    --rule: #c9ccd4;
    --photo-a: #c7d3e3;
    --photo-b: #eef2f7;
    --white: #ffffff;
  }
  * { box-sizing: border-box; margin: 0; padding: 0; }
  html, body { width: 853px; height: 1200px; overflow: hidden; background: var(--white); }
  body { font-family: "Open Sans", Arial, sans-serif; color: var(--text); }
  .leaflet { position: relative; width: 853px; height: 1200px; overflow: hidden; }

  .hero-photo {
    position: absolute; left: 0; top: 150px; width: 310px; height: 580px;
    background: radial-gradient(ellipse at 35% 45%, var(--photo-a) 0%, var(--photo-b) 55%, rgba(255,255,255,0) 78%);
  }

  .section-tab {
    position: absolute; left: 0; width: 853px; height: 30px;
  }
  .section-tab::before {
    content: ""; position: absolute; left: 40px; right: 40px; top: 14px; border-top: 1px solid var(--rule);
  }
  .section-tab span {
    position: absolute; left: 50%; transform: translateX(-50%); top: 0;
    background: var(--navy); color: var(--white); font-weight: 700; font-size: 15px; letter-spacing: 1px;
    padding: 5px 34px 6px; border-radius: 0 0 10px 10px; white-space: nowrap;
  }
  .section-tab.top::before { display: none; }
  .section-tab.mid span { border-radius: 10px; }

  .block { position: absolute; left: 45px; width: 763px; text-align: center; }
  .option-heading { color: var(--red); font-weight: 700; font-size: 15px; letter-spacing: .3px; margin-bottom: 10px; }
  .block p { font-size: 13px; line-height: 19px; }

  .after-column { position: absolute; left: 335px; top: 345px; width: 430px; }
  .after-column p { font-size: 13px; line-height: 19px; margin-bottom: 14px; }

  .questions { position: absolute; left: 60px; width: 733px; top: 865px; text-align: center; color: var(--navy); }
  .questions .lead { font-weight: 800; font-size: 16.5px; line-height: 23px; }
  .questions ul { list-style: none; margin-top: 16px; }
  .questions li { font-weight: 800; font-size: 16.5px; line-height: 26px; }

  .footer { position: absolute; left: 40px; right: 40px; top: 1085px; display: flex; justify-content: space-between; align-items: flex-end; }
  .hospital-name { color: var(--navy); font-weight: 600; font-size: 17px; line-height: 22px; }
  .doctor-name { color: var(--navy); font-weight: 800; font-size: 22px; letter-spacing: .5px; }
  .footer-rule { position: absolute; left: 40px; right: 40px; top: 1150px; border-top: 1px solid var(--rule); }
  .base-band { position: absolute; left: 0; bottom: 0; width: 853px; height: 16px; background: var(--navy); }
</style>
</head>
<body>
<main class="leaflet">
  <div class="hero-photo" role="img" aria-label="Photo of a hand giving a thumbs up"></div>

  <div class="section-tab top" style="top:0"><span>HOW IS IT DONE</span></div>

  <section class="block" style="top:52px">
    <h2 class="option-heading">IF YOU CHOOSE AWAKE SURGERY OR SURGERY WITH SEDATION</h2>
    <p>Numbing liquid is injected around the nerves which supply your foot. The ankle block takes 5 - 10 minutes to perform and requires 4 - 5 injections. Approximately 10 - 20 minutes to make your foot numb to pain. I will check the ankle block is working before we start surgery using cold spray. Sensations of touch, pressure, vibration and movement will still be felt. I will use a screen so you can't see the surgery (unless you would like to see). Some patients bring headphones to block out the noise of the operation.</p>
  </section>

  <section class="block" style="top:196px">
    <h2 class="option-heading">IF YOU CHOOSE A GENERAL ANAESTHETIC</h2>
    <p>I will perform the ankle block after I start the general anaesthetic. You should wake up from your surgery with a comfortable and numb foot/feet. If you wake in pain, we can repeat the ankle block or provide traditional painkillers.</p>
    <p>Whatever you choose, there will be a cannula placed in your hand and heart and oxygen monitoring throughout.</p>
  </section>

  <div class="section-tab mid" style="top:300px"><span>AFTER SURGERY</span></div>

  <section class="after-column">
    <p>You will go to the recovery area and then onto the ward when you are ready. It will be difficult to walk while the block is working so physiotherapists will help you first walk. If you need crutches they will teach you how to use them.</p>
    <p>Your foot will be numb and so you will not feel where your foot is in relation to nearby objects. As a result, it is easy to knock your foot. Please take extra care while your foot is still numb.</p>
    <p>As the block wears off, the foot may feel slightly painful, tingly or hot. At this point you should take the painkillers I have prescribed. Depending on your medical history you will have up to three painkillers. I would suggest starting with all three. You will also have an anti-sickness medicine prescribed if one of the painkillers (typically codeine or morphine) makes you feel sick.</p>
    <p>Occasionally, pain after the ankle block wears off will be significant. Please either contact the surgeon's secretary or myself and we can discuss the pain relief options.</p>
  </section>

  <div class="section-tab mid" style="top:735px"><span>THE ALTERNATIVE</span></div>

  <section class="block" style="top:780px">
    <p>If you do not have an ankle block your surgery can still proceed.<br>Post-operative pain can be managed with traditional painkillers.<br>However, you are more likely to need an overnight stay or feel sick after the anaesthetic.</p>
  </section>

  <section class="questions">
    <p class="lead">If you have any further questions about an ankle block I will see you the day of your surgery. Alternatively, you can request the following optional services (as mentioned in my terms of business).</p>
    <ul>
      <li>Email me your Questions</li>
      <li>Request a Pre operative telephone call</li>
      <li>Have a clinic appointment</li>
    </ul>
  </section>

  <footer class="footer">
    <div class="hospital-name">Kingsgate Hospital<br>part of Meridian Healthcare UK</div>
    <div class="doctor-name">DR TOBIAS WENDELL</div>
  </footer>
  <div class="footer-rule"></div>
  <div class="base-band"></div>
</main>
</body>
</html>
```